One page website for a Personal Injury Law Firm

Design and code a one page website in WordPress for the Darrow Law Firm, which is a a personal injury law firm located in Coral Gables, Florida. Please note: if you want to change the color pallete for the logo and for the web design , that is fine by me.

Target Market(s)

Those injured in accidents that need legal representation

Industry/Entity Type

Legal

Coding

Coded - Design and coding required

Number of Pages Required

1 page

Font styles to use
Other font styles liked:
• Montserrat

```html
<!DOCTYPE html>
<html lang="en">
<head>
<meta charset="utf-8">
<title>Darrow Law Firm – Personal Injury Attorneys, Coral Gables</title>
<link href="https://fonts.googleapis.com/css2?family=Montserrat:wght@400;500;600;700&family=Poppins:wght@400;500;600&display=swap" rel="stylesheet">
<style>
:root{
  --ink:#211d2f;
  --ink-2:#2a2638;
  --tan:#cfa06f;
  --gold:#c4965f;
  --white:#ffffff;
  --text:#2b2b35;
  --muted:#55555f;
  --line:#e6e4ea;
  --card-line:#3b3750;
}
*{box-sizing:border-box;margin:0;padding:0}
html,body{width:1200px;height:4421px;overflow:hidden}
body{position:relative;background:var(--white);font-family:"Poppins",sans-serif;color:var(--text)}
.abs{position:absolute}
h1,h2,h3,h4{font-family:"Montserrat",sans-serif;font-weight:500}
.brand{display:flex;align-items:center;gap:10px;color:var(--white);font-family:"Montserrat",sans-serif;font-weight:600;font-size:24px;letter-spacing:.5px}
.brand-dot{width:22px;height:22px;border:2px solid var(--white);border-radius:50%}
.nav{display:flex;gap:34px;font-size:13px;color:var(--white)}
.btn{display:inline-block;background:var(--tan);color:var(--ink);font-family:"Montserrat",sans-serif;font-weight:700;font-size:14px;padding:14px 22px;border-radius:3px;box-shadow:5px 5px 0 -1px var(--white),5px 5px 0 0 var(--tan)}
.photo{border-radius:4px}
.rule{left:0;width:1200px;height:1px;background:var(--line)}
.section-title{font-size:36px;color:var(--ink);line-height:1.2}
.section-sub{font-size:19px;color:var(--muted);font-family:"Montserrat",sans-serif;margin-top:6px}
.hex{width:76px;height:82px}
.why-card{border:1px solid var(--card-line);border-radius:6px;padding:58px 22px 20px;color:#d9d6e2;font-size:12.5px;line-height:2}
.why-card h4{color:var(--white);font-size:15px;font-weight:600;line-height:1.6;margin-bottom:6px}
.why-card.active{background:var(--white);color:var(--muted);border-color:var(--white)}
.why-card.active h4{color:var(--ink)}
.strat-title{font-family:"Montserrat",sans-serif;font-weight:600;font-size:25px;line-height:1.45;color:var(--ink)}
.strat-text{font-size:12.5px;line-height:2;color:var(--muted)}
.area{border:1px solid var(--card-line);border-radius:4px;text-align:center;color:var(--white);font-size:14px;line-height:1.45;padding-top:18px}
.area .hex{width:56px;height:60px;margin:0 auto 16px}
.area .more{position:absolute;left:0;right:0;bottom:18px;color:var(--tan);font-size:12px;font-weight:600}
.area.active{background:var(--white);color:var(--ink);border-color:var(--white)}
.area.active b{display:block;font-size:15px;margin-bottom:6px;font-weight:600}
.area.active p{font-size:12px;color:var(--muted);line-height:2;padding:0 14px}
.foot-h{font-family:"Montserrat",sans-serif;font-size:19px;color:var(--white);font-weight:500}
.foot-line{display:flex;align-items:flex-start;gap:12px;color:#e4e1ea;font-size:12.5px;line-height:1.7}
.social{width:32px;height:32px;border-radius:50%;border:1.5px solid var(--white)}
</style>
</head>
<body>

<!-- Header + hero -->
<section class="abs" style="left:0;top:0;width:1200px;height:615px;background:var(--ink);border-bottom-left-radius:90px" aria-label="Introduction">
  <div class="abs brand" style="left:120px;top:34px"><span class="brand-dot"></span>Darrow</div>
  <nav class="abs nav" style="left:335px;top:40px">
    <span>Home</span><span>About Us</span><span>Our Strategy</span><span>Our Practice Areas</span><span>Contact Us</span>
  </nav>
  <svg class="abs" style="left:864px;top:38px" width="20" height="20" viewBox="0 0 20 20" fill="none" stroke="#fff" stroke-width="1.6"><circle cx="8.5" cy="8.5" r="6"/><path d="M13 13l5 5"/></svg>
  <div class="abs" style="left:850px;top:28px;width:1px;height:40px;background:#55516a"></div>
  <span class="abs btn" style="left:903px;top:22px">Free Consultation</span>
  <div class="abs" style="left:0;top:96px;width:1200px;height:1px;background:#36324a"></div>

  <h1 class="abs" style="left:120px;top:155px;width:700px;font-size:50px;line-height:1.15;color:var(--white)">Justice. Recovery. A Better Future Starts Here.</h1>
  <p class="abs" style="left:120px;top:278px;width:470px;font-size:12px;line-height:2;color:#e2dfe8">At The Darrow Law Firm, We Understand That Suffering A Personal Injury Can Be Life-Altering—Physically, Emotionally, And Financially. You May Be Unsure Whether Pursuing Legal Action Is The Right Step. But In Florida, Holding Negligent Parties Accountable Isn't Just Your Right—It's Often Necessary To Rebuild Your Life.</p>
  <span class="abs btn" style="left:120px;top:428px;padding:15px 46px">Learn More</span>
  <div class="abs" style="left:312px;top:430px;width:48px;height:48px;border-radius:50%;background:var(--white)"></div>
  <svg class="abs" style="left:324px;top:442px" width="24" height="24" viewBox="0 0 24 24" fill="none" stroke="#211d2f" stroke-width="1.5"><path d="M5 3h4l2 5-2.5 1.5a11 11 0 005 5L15 12l5 2v4a2 2 0 01-2 2A16 16 0 013 5a2 2 0 012-2z"/></svg>
  <div class="abs" style="left:372px;top:434px;color:var(--white);font-size:12px;line-height:1.8">Free Consultation<br><span style="color:#cfccd8">(786) 555-0182</span></div>
</section>
<div class="abs photo" role="img" aria-label="Attorney and client reviewing documents at a desk" style="left:613px;top:224px;width:465px;height:439px;background:linear-gradient(135deg,#3a3330,#8a7c70 55%,#d8d2c8)"></div>

<!-- Why choose -->
<h2 class="abs section-title" style="left:120px;top:684px">Why Choose The<br>Darrow Law Firm?</h2>
<div class="abs rule" style="top:788px"></div>

<div class="abs" style="left:0;top:1237px;width:1200px;height:476px;background:var(--ink);border-top-right-radius:90px"></div>
<div class="abs photo" role="img" aria-label="Classical stone columns under a blue sky" style="left:120px;top:825px;width:464px;height:472px;background:linear-gradient(160deg,#9fc1e6,#d9cfc0 45%,#a89a86)"></div>
<div class="abs" style="left:644px;top:848px;width:400px">
  <h3 style="font-size:19.5px;line-height:1.45;color:var(--ink);font-weight:600">Unmatched Experience. Proven Results. Relentless Advocacy.</h3>
  <p style="font-size:12.5px;line-height:2;color:var(--muted);margin-top:12px">A client fell eight feet at a major sporting venue and suffered catastrophic injuries. We recovered compensation that covered all medical bills, paid off their home, and funded their children's college education.</p>
  <p style="font-size:12.5px;line-height:2;color:var(--muted)">A Client suffered a severe infection from a minor slip-and-fall injury in a miami condo building. We resolved the case before filing a lawsuit, securing funds that allowed him to buy a new home, pay off debts, and provide private school tuition for his children.</p>
  <span class="btn" style="margin-top:22px;padding:13px 22px">Free Consultation</span>
</div>

<div class="abs why-card" style="left:120px;top:1395px;width:308px;height:270px"><h4>25+ Years Of Legal Mastery:</h4>We have successfully handled thousands of cases, fighting both for and against insurance companies. This unique dual experience gives us an insider advantage in every case we take on.</div>
<div class="abs why-card active" style="left:446px;top:1395px;width:308px;height:270px"><h4>Extensive Knowledge Of Insurance Tactics:</h4>Having worked for insurance companies, we know their strategies, loopholes, and how to dismantle their defenses to maximize your settlement.</div>
<div class="abs why-card" style="left:771px;top:1395px;width:308px;height:270px"><h4>Millions Recovered For Clients:</h4>Millions Recovered For Clients</div>
<svg class="abs hex" style="left:151px;top:1352px" viewBox="0 0 76 82"><path d="M38 2l34 20v38L38 80 4 60V22z" fill="#fff"/><circle cx="30" cy="38" r="6" fill="#cfa06f"/><circle cx="46" cy="38" r="6" fill="#cfa06f"/><path d="M20 56a10 10 0 0120 0zM36 56a10 10 0 0120 0z" fill="#cfa06f"/></svg>
<svg class="abs hex" style="left:477px;top:1352px" viewBox="0 0 76 82"><path d="M38 2l34 20v38L38 80 4 60V22z" fill="#fff" stroke="#211d2f" stroke-width="2"/><path d="M38 22l14 6v10c0 9-6 15-14 18-8-3-14-9-14-18V28z" fill="#cfa06f"/><path d="M31 39l5 5 9-10" stroke="#fff" stroke-width="3" fill="none"/></svg>
<svg class="abs hex" style="left:802px;top:1352px" viewBox="0 0 76 82"><path d="M38 2l34 20v38L38 80 4 60V22z" fill="#fff"/><circle cx="26" cy="50" r="7" fill="#cfa06f"/><circle cx="42" cy="50" r="7" fill="#cfa06f"/><path d="M20 38l12-8 8 5 14-12" stroke="#cfa06f" stroke-width="3" fill="none"/></svg>

<!-- Strategy -->
<div class="abs" style="left:120px;top:1772px"><h2 class="section-title">Our Strategy:</h2><p class="section-sub">Aggressive, Client-Focused, And Results-Driven</p></div>
<div class="abs rule" style="top:1872px"></div>

<div class="abs" style="left:0;top:1907px;width:1200px;height:245px;background:var(--tan)"></div>
<div class="abs photo" role="img" aria-label="Attorneys standing outside an office building" style="left:120px;top:1907px;width:326px;height:245px;border-radius:0;background:linear-gradient(150deg,#b7b3a8,#5e6670 60%,#6d7a52)"></div>
<div class="abs strat-title" style="left:493px;top:1990px;color:var(--white)">Taking On<br>Corporate Giants:</div>
<p class="abs strat-text" style="left:790px;top:1982px;width:290px;color:#fff4e6">We Don't Back Down From Big Insurance Companies, Property Management Firms, Or Major Corporations. We Fight For Justice—No Matter How Powerful The Opposition.</p>

<div class="abs" style="left:1129px;top:1965px;width:2px;height:570px;background:#e8e6ec"></div>
<div class="abs" style="left:1129px;top:1965px;width:2px;height:156px;background:var(--white)"></div>
<div class="abs" style="left:1120px;top:2112px;width:20px;height:20px;border-radius:50%;background:var(--white);border:1px solid var(--ink);font-size:8px;text-align:center;line-height:18px;color:var(--ink)">01</div>

<div class="abs photo" role="img" aria-label="Lawyer consulting with a client over documents" style="left:120px;top:2191px;width:326px;height:245px;border-radius:0;background:linear-gradient(135deg,#4a3a2e,#8b6f58 55%,#2c2a2c)"></div>
<div class="abs strat-title" style="left:493px;top:2275px">Concierge-Style<br>Legal Care:</div>
<p class="abs strat-text" style="left:778px;top:2265px;width:290px">You're Not Just Another Case Number. We Provide Dedicated, Personalized Service, Keeping You Informed, Supported, And Empowered Throughout The Legal Process.</p>

<div class="abs photo" role="img" aria-label="Advisor meeting with a couple in a bright office" style="left:120px;top:2475px;width:326px;height:245px;border-radius:0;background:linear-gradient(135deg,#c9b79c,#e9e3d8 55%,#8a8f98)"></div>
<div class="abs strat-title" style="left:493px;top:2560px">No Win, No Fee<br>Guarantee:</div>
<p class="abs strat-text" style="left:790px;top:2562px;width:290px">We Take Your Case On A Contingency Basis, Which Means You Pay Nothing Unless We Win.</p>

<!-- Practice areas -->
<section class="abs" style="left:0;top:2760px;width:1200px;height:730px;background:var(--ink);border-top-left-radius:90px" aria-label="Practice areas">
  <div class="abs" style="left:120px;top:50px"><h2 class="section-title" style="color:var(--white)">Our Practice Areas:</h2><p class="section-sub" style="color:#d9d6e2">Comprehensive Representation For The Injured</p></div>
  <div class="abs" style="left:0;top:155px;width:1200px;height:1px;background:#36324a"></div>
</section>
<div class="abs area" style="left:172px;top:2960px;width:198px;height:188px"><svg class="hex" viewBox="0 0 56 60"><path d="M28 2l25 15v27L28 58 3 44V17z" fill="#fff"/><path d="M18 40h22M24 22l6 10-8 6" stroke="#cfa06f" stroke-width="3" fill="none"/><circle cx="24" cy="18" r="3" fill="#cfa06f"/></svg>Slip And Fall /<br>Premises Liability:<span class="more">Learn More &gt;&gt;</span></div>
<div class="abs area" style="left:392px;top:2960px;width:198px;height:188px"><svg class="hex" viewBox="0 0 56 60"><path d="M28 2l25 15v27L28 58 3 44V17z" fill="#fff"/><rect x="16" y="26" width="24" height="10" rx="3" fill="#cfa06f"/><circle cx="21" cy="38" r="3" fill="#cfa06f"/><circle cx="35" cy="38" r="3" fill="#cfa06f"/></svg>Car Accidents:<span class="more">Learn More &gt;&gt;</span></div>
<div class="abs area" style="left:610px;top:2960px;width:198px;height:188px"><svg class="hex" viewBox="0 0 56 60"><path d="M28 2l25 15v27L28 58 3 44V17z" fill="#fff"/><path d="M14 34c6 0 10 4 16 4l12-6" stroke="#cfa06f" stroke-width="3" fill="none"/><circle cx="30" cy="23" r="5" fill="#cfa06f"/></svg>Wrongful Death:<span class="more">Learn More &gt;&gt;</span></div>
<div class="abs area" style="left:830px;top:2960px;width:198px;height:188px"><svg class="hex" viewBox="0 0 56 60"><path d="M28 2l25 15v27L28 58 3 44V17z" fill="#fff"/><path d="M28 18l12 6v14l-12 6-12-6V24z" fill="#cfa06f"/></svg>Product Liability:<span class="more">Learn More &gt;&gt;</span></div>

<div class="abs area" style="left:155px;top:3204px;width:198px;height:186px"><svg class="hex" viewBox="0 0 56 60"><path d="M28 2l25 15v27L28 58 3 44V17z" fill="#fff"/><path d="M14 38h28l-4 6H18zM26 18v18l10-4z" fill="#cfa06f"/></svg>Boating And<br>Watercraft Accidents:<span class="more">Learn More &gt;&gt;</span></div>
<div class="abs area active" style="left:375px;top:3168px;width:231px;height:257px;padding-top:22px"><svg class="hex" viewBox="0 0 56 60"><path d="M28 2l25 15v27L28 58 3 44V17z" fill="#cfa06f"/><circle cx="24" cy="24" r="5" fill="#fff"/><path d="M20 42l6-12 10 4" stroke="#fff" stroke-width="3" fill="none"/></svg><b>Dog Bites And<br>Animal Attacks:</b><p>Florida's strict liability laws mean pet owners are responsible for injuries caused by their animals.</p></div>
<div class="abs area" style="left:628px;top:3204px;width:198px;height:186px"><svg class="hex" viewBox="0 0 56 60"><path d="M28 2l25 15v27L28 58 3 44V17z" fill="#fff"/><circle cx="28" cy="20" r="4" fill="#cfa06f"/><rect x="22" y="26" width="12" height="16" rx="2" fill="#cfa06f"/></svg>Workplace Injuries<br>(Third-Party Claims):<span class="more">Learn More &gt;&gt;</span></div>
<div class="abs area" style="left:846px;top:3204px;width:198px;height:186px"><svg class="hex" viewBox="0 0 56 60"><path d="M28 2l25 15v27L28 58 3 44V17z" fill="#fff"/><rect x="14" y="24" width="18" height="12" fill="#cfa06f"/><path d="M32 28h6l4 5v3H32z" fill="#cfa06f"/><circle cx="20" cy="38" r="3" fill="#cfa06f"/><circle cx="37" cy="38" r="3" fill="#cfa06f"/></svg>Truck , Commercial<br>Vehicle Accidents:<span class="more">Learn More &gt;&gt;</span></div>

<!-- Florida law -->
<div class="abs" style="left:120px;top:3548px"><h2 class="section-title">Florida Personal Injury Law:</h2><p class="section-sub">What You Need To Know</p></div>
<svg class="abs" style="left:992px;top:3576px" width="86" height="34" viewBox="0 0 86 34" fill="none" stroke="#cfa06f" stroke-width="1.5"><circle cx="17" cy="17" r="15"/><path d="M24 17H10m5-5l-5 5 5 5"/><rect x="34" y="2" width="50" height="30" rx="15"/><path d="M48 17h22m-5-5l5 5-5 5"/></svg>
<div class="abs rule" style="top:3650px"></div>
<div class="abs photo" role="img" aria-label="Attorney seated at a desk with a gavel and bookshelves behind" style="left:122px;top:3685px;width:464px;height:310px;background:linear-gradient(135deg,#d9d4cb,#6a5646 50%,#2e2a2a)"></div>
<div class="abs" style="left:668px;top:3750px;width:420px">
  <div style="color:var(--tan);font-size:14px;font-weight:600">01.</div>
  <h3 style="font-size:20px;color:var(--ink);font-weight:600;margin-top:14px">Your Rights And Legal Protections</h3>
  <p style="font-size:14.5px;color:var(--muted);margin-top:10px;font-family:'Montserrat',sans-serif">Comparative Negligence <span style="color:var(--tan)">(Florida Statutes §768.81):</span></p>
  <p style="font-size:12px;line-height:2;color:var(--muted);margin-top:12px">Even If You Were Partially At Fault, You Can Still Recover Compensation. Your Damages Will Be Reduced Based On Your Percentage Of Fault.</p>
</div>

<!-- Footer -->
<footer class="abs" style="left:0;top:4025px;width:1200px;height:396px;background:var(--ink);border-top-right-radius:90px">
  <div class="abs brand" style="left:120px;top:78px;font-size:28px"><span class="brand-dot"></span>Darrow</div>
  <nav class="abs nav" style="left:489px;top:80px">
    <span>Home</span><span>About Us</span><span>Our Strategy</span><span>Our Practice Areas</span><span>Contact Us</span>
  </nav>
  <div class="abs foot-h" style="left:120px;top:185px">Contact Us</div>
  <div class="abs" style="left:120px;top:228px;display:flex;flex-direction:column;gap:16px">
    <div class="foot-line"><svg width="18" height="18" viewBox="0 0 18 18" fill="none" stroke="#fff" stroke-width="1.4"><path d="M9 17s6-6 6-10A6 6 0 003 7c0 4 6 10 6 10z"/><circle cx="9" cy="7" r="2"/></svg><span>418 Mirella Avenue, Coral<br>Gables, FL 33134</span></div>
    <div class="foot-line"><svg width="18" height="18" viewBox="0 0 18 18" fill="none" stroke="#fff" stroke-width="1.4"><rect x="2" y="4" width="14" height="10" rx="1"/><path d="M2 5l7 5 7-5"/></svg><span>info@darrowlawfirm.com</span></div>
    <div class="foot-line"><svg width="18" height="18" viewBox="0 0 24 24" fill="none" stroke="#fff" stroke-width="1.6"><path d="M5 3h4l2 5-2.5 1.5a11 11 0 005 5L15 12l5 2v4a2 2 0 01-2 2A16 16 0 013 5a2 2 0 012-2z"/></svg><span>(786) 555-0182</span></div>
  </div>
  <div class="abs foot-h" style="left:415px;top:185px">Social Links</div>
  <div class="abs" style="left:415px;top:228px;display:flex;gap:10px">
    <span class="social" aria-label="Social link 1"></span>
    <span class="social" aria-label="Social link 2" style="background:var(--tan);border-color:var(--tan)"></span>
    <span class="social" aria-label="Social link 3"></span>
    <span class="social" aria-label="Social link 4"></span>
  </div>
  <div class="abs" style="left:695px;top:222px;color:var(--white);font-size:13px">Let's Stay In Touch</div>
  <div class="abs" style="left:695px;top:262px;width:330px;border-bottom:1px solid #55516a;padding-bottom:8px;color:#8f8ba0;font-size:12.5px">Enter Email</div>
  <div class="abs" style="left:1027px;top:252px;width:52px;height:38px;background:var(--tan);border-radius:3px"></div>
  <svg class="abs" style="left:1043px;top:261px" width="20" height="20" viewBox="0 0 20 20" fill="none" stroke="#fff" stroke-width="1.8"><path d="M3 10h13m-5-5l5 5-5 5"/></svg>
  <div class="abs" style="left:0;top:362px;width:1200px;height:1px;background:#36324a"></div>
  <div class="abs" style="left:0;top:372px;width:1200px;text-align:center;color:#e4e1ea;font-size:12px">Free Consultation | No Fees Unless We Win | Aggressive Representation</div>
</footer>

</body>
</html>
```